Tre Nuvole Leaf Design Business Card/Hang Tag

Design a 3.5" X 2" (Leaf Shaped-See Files) Business Card/ Hang Tag that will have our Business Logo and Info on the Front, and will have On-Line Delivery Logos and Info on the Rear.

```html
<!DOCTYPE html>
<html lang="en">
<head>
<meta charset="utf-8">
<title>Tre Nuvole Restaurant – Business Card / Hang Tag</title>
<link rel="stylesheet" href="https://fonts.googleapis.com/css2?family=Lobster&display=swap">
<style>
  :root {
    --page-bg: #efefef;
    --garden-pink: #f1c6cf;
    --garden-rose: #e79aab;
    --garden-green: #c9dcc0;
    --garden-path: #e9ede1;
    --wash: rgba(255, 255, 255, 0.55);
    --logo-red: #c3202c;
    --logo-green: #2c6e36;
    --info-green: #2f7a3a;
    --badge-bg: #ffffff;
    --badge-text: #b8232d;
  }
  * { box-sizing: border-box; margin: 0; padding: 0; }
  html, body { width: 1200px; height: 757px; overflow: hidden; }
  body {
    background: var(--page-bg);
    font-family: "Lobster", cursive;
    position: relative;
  }
  .card {
    position: absolute;
    top: 199px;
    width: 512px;
    height: 296px;
    overflow: hidden;
  }
  .card--front { left: 77px; border-radius: 0 130px 0 130px; }
  .card--back  { left: 624px; width: 508px; border-radius: 130px 0 130px 0; }

  .card__garden {
    position: absolute; inset: 0;
    background:
      radial-gradient(ellipse 40% 60% at 12% 35%, var(--garden-rose), transparent 70%),
      radial-gradient(ellipse 40% 60% at 88% 35%, var(--garden-rose), transparent 70%),
      radial-gradient(ellipse 30% 35% at 50% 90%, var(--garden-path), transparent 80%),
      linear-gradient(180deg, var(--garden-pink) 0%, var(--garden-green) 70%, var(--garden-green) 100%);
  }
  .card__garden::after {
    content: ""; position: absolute; inset: 0; background: var(--wash);
  }

  .brand {
    position: absolute;
    left: 0; right: 0;
    text-align: center;
    color: var(--logo-red);
    line-height: 1;
  }
  .brand__name { display: block; font-size: 40px; }
  .brand__type { display: block; font-size: 24px; margin-top: 6px; color: var(--logo-red); }
  .card--front .brand { top: 118px; }
  .card--back .brand { top: 118px; }

  .website {
    position: absolute;
    left: 0; right: 0; bottom: 30px;
    text-align: center;
    font-size: 19px;
    color: var(--logo-red);
    letter-spacing: 0.3px;
  }

  .contact {
    position: absolute;
    right: 78px; bottom: 18px;
    text-align: center;
    color: var(--info-green);
    font-size: 17px;
    line-height: 1.22;
    font-style: normal;
  }

  .delivery {
    position: absolute;
    left: 10px; bottom: 12px;
    display: flex; gap: 6px;
    list-style: none;
  }
  .delivery__item {
    width: 64px; height: 38px;
    background: var(--badge-bg);
    border-radius: 9px;
    display: flex; align-items: center; justify-content: center;
    text-align: center;
    font-size: 10px; line-height: 1.05;
    color: var(--badge-text);
    padding: 3px;
  }
  .delivery__item--narrow { width: 38px; font-size: 8px; }
</style>
</head>
<body>
  <section class="card card--front" aria-label="Card front">
    <div class="card__garden" role="img" aria-label="Soft-focus photograph of a rose garden archway with a hedged path"></div>
    <h1 class="brand">
      <span class="brand__name">Tre Nuvole</span>
      <span class="brand__type">Restaurant</span>
    </h1>
    <p class="website">www.trenuvoletable.com</p>
  </section>

  <section class="card card--back" aria-label="Card back">
    <div class="card__garden" role="img" aria-label="Soft-focus photograph of a rose garden archway with a hedged path"></div>
    <p class="brand">
      <span class="brand__name">Tre Nuvole</span>
      <span class="brand__type">Restaurant</span>
    </p>
    <ul class="delivery" aria-label="Order online with">
      <li class="delivery__item">Forkrunner</li>
      <li class="delivery__item">Porchdrop</li>
      <li class="delivery__item delivery__item--narrow">Courier Bites</li>
    </ul>
    <address class="contact">
      418 Alder Street<br>
      Fernvale, California 94990<br>
      (555) 014-2276
    </address>
  </section>
</body>
</html>
```